Disability provider requiring digital flyer to promote services

My company works within the Disability sector (QCWP registered provider), currently operating in Sydney, Australia.
I require a digital brochure which lists our services and gives potential customers a quick look into what we do with a single glance.
Undecided whether this digital flyer is to be single or double sided, happy to consult with an experienced designer in this regard.
I prefer minimalist designs (which may be an issue for someone trying to convey information, I'm not sure), and possibly someone who can work with out watercolor logo.
Services include:
-Supported Independent Living
-Specialist Disability Accommodation
-Individualised Living Options Stage 1 & 2
-Home Modifications
-Occupational Therapy
-Support Coordination Levels 1 & 2
-Short Term Accommodation - STA Respite
-Drop In Supports
-Community Access

```html
<!DOCTYPE html>
<html lang="en">
<head>
<meta charset="utf-8">
<title>Clearview Care – Flyer</title>
<link href="https://fonts.googleapis.com/css2?family=Montserrat:wght@400;500;600;700;800;900&display=swap" rel="stylesheet">
<style>
:root{
  --stage:#d8d8d8;
  --orange:#f5874a;
  --teal:#17b895;
  --ink:#1f1f1f;
  --sky-top:#f4fbfd;
  --sky-mid:#c9eff6;
  --sky-deep:#a9e4ef;
  --grass:#6fae3a;
  --grass-light:#b9d98a;
}
*{margin:0;padding:0;box-sizing:border-box}
html,body{width:1200px;height:2531px;overflow:hidden;background:var(--stage)}
body{font-family:"Montserrat",sans-serif;color:var(--ink);position:relative}
.flyer{
  position:absolute;left:80px;top:528px;width:1040px;height:1474px;overflow:hidden;
  background:
    radial-gradient(ellipse 520px 380px at 820px 620px,var(--sky-deep),transparent 70%),
    radial-gradient(ellipse 600px 420px at 180px 900px,var(--sky-mid),transparent 70%),
    linear-gradient(180deg,var(--sky-top) 0%,#dff5fa 40%,var(--sky-mid) 100%);
  box-shadow:0 20px 40px rgba(0,0,0,.35);
}
.brand{position:absolute;left:67px;top:250px;width:323px;display:flex;align-items:center;gap:14px}
.brand-dot{width:26px;height:26px;border-radius:50%;background:var(--teal);flex:none}
.brand-name{font-weight:600;font-size:40px;letter-spacing:1px;color:var(--teal)}
.hero{position:absolute;left:565px;top:109px;width:440px}
.hero-title{font-weight:800;font-size:52px;line-height:56px;color:var(--teal)}
.hero-title .accent{color:var(--orange)}
.hero-sub{margin-top:22px;font-size:22px;line-height:30px;font-weight:500}
.hero-sub .place{color:var(--teal);font-weight:600}
.section-title{font-weight:700;font-size:32px;line-height:41px;color:var(--orange)}
.section-title .alt{color:var(--teal)}
.about{position:absolute;left:67px;top:428px;width:410px}
.about-text{margin-top:12px;font-size:18.5px;line-height:24px;font-weight:500;text-align:justify}
.hours{margin-top:26px;border-left:3px solid var(--teal);padding-left:12px;font-size:21px;line-height:28px;font-weight:500}
.hours-label{color:var(--teal);font-weight:600}
.contacts{margin-top:26px;list-style:none;font-size:18px;line-height:27px;font-weight:500}
.contacts li{display:flex;align-items:center;gap:12px}
.contacts .strong{font-weight:700}
.contacts .hl{color:var(--teal);font-weight:600}
.icon{width:20px;height:20px;flex:none}
.services{position:absolute;left:565px;top:428px;width:450px}
.service-list{margin-top:10px;list-style:none;font-size:18.5px;line-height:31px;font-weight:500}
.service-list li{display:flex;align-items:center;gap:14px}
.tick{width:14px;height:14px;flex:none}
.scene{position:absolute;left:0;top:754px;width:1040px;height:720px}
</style>
</head>
<body>
<main class="flyer">
  <div class="brand"><span class="brand-dot"></span><span class="brand-name">CLEARVIEW CARE</span></div>

  <section class="hero">
    <h1 class="hero-title"><span class="accent">Clearview</span> for an empowered future</h1>
    <p class="hero-sub">Disability sector (QCWP registered provider), currently operating in <span class="place">Sydney, Australia</span></p>
  </section>

  <section class="about">
    <h2 class="section-title">What is Clearview<br><span class="alt">Care about</span></h2>
    <p class="about-text">Clearview Care is a Sydney based disability support services provider. Focusing on intellectual, physical &amp; sensory disabilities including mental health within the greater Sydney region, we strive to assist our participants in leading an independent and fulfilling life.</p>
    <div class="hours"><div class="hours-label">Operating Hours:</div><div>9AM To 5PM&nbsp; Monday - Friday</div></div>
    <ul class="contacts">
      <li><svg class="icon" viewBox="0 0 20 20"><circle cx="10" cy="10" r="8.5" fill="none" stroke="#f5874a" stroke-width="1.5"/><path d="M7 6l2 2-1 1.3c.6 1.2 1.5 2.1 2.7 2.7L12 11l2 2-1.3 1.3C9.5 14 6 10.5 5.7 7.3Z" fill="#f5874a"/></svg><span class="strong">+61 0400 123 456</span></li>
      <li><svg class="icon" viewBox="0 0 20 20"><circle cx="10" cy="10" r="8.5" fill="none" stroke="#f5874a" stroke-width="1.5"/><rect x="5.5" y="7" width="9" height="6.5" rx="1" fill="#f5874a"/><path d="M5.8 7.5 10 10.5l4.2-3" stroke="#fff" fill="none"/></svg><span>info@<span class="hl">clearviewcare</span>.com.au</span></li>
      <li><svg class="icon" viewBox="0 0 20 20"><circle cx="10" cy="10" r="8.5" fill="none" stroke="#f5874a" stroke-width="1.5"/><circle cx="10" cy="10" r="5" fill="none" stroke="#f5874a" stroke-width="1.3"/><path d="M5 10h10M10 5c-2 3-2 7 0 10M10 5c2 3 2 7 0 10" stroke="#f5874a" fill="none"/></svg><span>www.<span class="hl">clearviewcare</span>.com.au</span></li>
    </ul>
  </section>

  <section class="services">
    <h2 class="section-title">What we do</h2>
    <ul class="service-list">
      <li><svg class="tick" viewBox="0 0 14 14"><circle cx="7" cy="7" r="7" fill="#17b895"/><path d="M4 7.2l2 2 4-4" stroke="#fff" stroke-width="1.6" fill="none"/></svg>Supported Independent Living</li>
      <li><svg class="tick" viewBox="0 0 14 14"><circle cx="7" cy="7" r="7" fill="#17b895"/><path d="M4 7.2l2 2 4-4" stroke="#fff" stroke-width="1.6" fill="none"/></svg>Specialist Disability Accommodation</li>
      <li><svg class="tick" viewBox="0 0 14 14"><circle cx="7" cy="7" r="7" fill="#17b895"/><path d="M4 7.2l2 2 4-4" stroke="#fff" stroke-width="1.6" fill="none"/></svg>Individualised Living Options Stage 1 &amp; 2</li>
      <li><svg class="tick" viewBox="0 0 14 14"><circle cx="7" cy="7" r="7" fill="#17b895"/><path d="M4 7.2l2 2 4-4" stroke="#fff" stroke-width="1.6" fill="none"/></svg>Home Modifications</li>
      <li><svg class="tick" viewBox="0 0 14 14"><circle cx="7" cy="7" r="7" fill="#17b895"/><path d="M4 7.2l2 2 4-4" stroke="#fff" stroke-width="1.6" fill="none"/></svg>Occupational Therapy</li>
      <li><svg class="tick" viewBox="0 0 14 14"><circle cx="7" cy="7" r="7" fill="#17b895"/><path d="M4 7.2l2 2 4-4" stroke="#fff" stroke-width="1.6" fill="none"/></svg>Support Coordination Levels 1 &amp; 2</li>
      <li><svg class="tick" viewBox="0 0 14 14"><circle cx="7" cy="7" r="7" fill="#17b895"/><path d="M4 7.2l2 2 4-4" stroke="#fff" stroke-width="1.6" fill="none"/></svg>Short Term Accommodation - STA Respite</li>
      <li><svg class="tick" viewBox="0 0 14 14"><circle cx="7" cy="7" r="7" fill="#17b895"/><path d="M4 7.2l2 2 4-4" stroke="#fff" stroke-width="1.6" fill="none"/></svg>Drop In Supports</li>
      <li><svg class="tick" viewBox="0 0 14 14"><circle cx="7" cy="7" r="7" fill="#17b895"/><path d="M4 7.2l2 2 4-4" stroke="#fff" stroke-width="1.6" fill="none"/></svg>Community Access</li>
    </ul>
  </section>

  <svg class="scene" viewBox="0 0 1040 720" preserveAspectRatio="none">
    <defs>
      <linearGradient id="park" x1="0" y1="0" x2="0" y2="1">
        <stop offset="0" stop-color="#d9ecd0"/>
        <stop offset=".35" stop-color="#a9cf7e"/>
        <stop offset=".7" stop-color="#6fae3a"/>
        <stop offset="1" stop-color="#8fc24f"/>
      </linearGradient>
    </defs>
    <path role="img" aria-label="Photo of a smiling carer hugging an elderly woman in a wheelchair in a sunny park" fill="url(#park)" d="M0,230 C120,160 260,150 390,200 C520,250 640,170 760,120 C860,80 960,60 1040,90 L1040,720 L0,720 Z"/>
    <path fill="#17b895" d="M300,215 C420,100 600,55 770,115 C660,150 570,200 470,222 C400,236 340,230 300,215Z"/>
    <path fill="#17b895" d="M0,300 L0,245 C25,236 45,232 70,232 C40,250 20,272 0,300Z"/>
    <path fill="#f5874a" d="M820,100 C900,40 980,28 1040,38 L1040,105 C980,78 900,78 820,100Z"/>
  </svg>
</main>
</body>
</html>
```